Residential Roofing Company, need a Unique business card for a Woman owned ompany

Woman Owned Residential Roofing Company. Specializing in Insurance Claims
Attention to Detail is what sets this woman owned roofing company apart from the rest
We are TRV Certified and are an Accredited business with an A rating with the QPL. Our Contractor License number KMT48395

```html
<!DOCTYPE html>
<html lang="en">
<head>
<meta charset="utf-8">
<title>Ridgecrest Roofing – Business Card</title>
<link href="https://fonts.googleapis.com/css2?family=Montserrat:wght@800&family=Open+Sans:wght@400;600&display=swap" rel="stylesheet">
<style>
  :root{
    --backdrop:#3a3a3a;
    --card:#161616;
    --accent:#1f7fc0;
    --accent-navy:#2b3f86;
    --ink:#f2f2f2;
    --wordmark:#2e2e2e;
  }
  *{margin:0;padding:0;box-sizing:border-box}
  html,body{width:1200px;height:801px;overflow:hidden}
  body{background:var(--backdrop);position:relative;font-family:"Open Sans",sans-serif}
  .card{position:absolute;width:520px;height:297px;background:var(--card);
        border-bottom:3px solid var(--accent);box-shadow:0 10px 24px rgba(0,0,0,.35);overflow:hidden}
  .card--front{left:60px;top:150px}
  .card--back{left:620px;top:354px}

  /* front side */
  .brand-panel{position:absolute;left:0;top:0;width:255px;height:100%;padding:0 24px;
               display:flex;align-items:center;justify-content:center;gap:12px}
  .brand-mark{width:16px;height:16px;flex:none;background:var(--accent-navy)}
  .brand-name{font-family:"Montserrat",sans-serif;font-weight:800;font-size:21px;line-height:1.2;color:var(--ink);letter-spacing:.5px}
  .divider{position:absolute;left:255px;top:36px;width:1.5px;height:225px;background:var(--accent)}
  .contact{position:absolute;left:280px;top:40px;color:var(--ink);font-size:12.5px;line-height:1.45}
  .contact__name{font-weight:600;font-size:19px;color:var(--accent);letter-spacing:.5px;line-height:1.1}
  .contact__role{margin-bottom:8px}
  .contact__license{color:var(--accent);margin-bottom:8px}
  .contact__line{display:flex;align-items:center;gap:7px}
  .contact__line svg{width:12px;height:12px;flex:none}
  .badge{position:absolute;right:26px;bottom:24px;width:64px;height:26px;border-radius:3px;background:var(--accent)}

  /* back side */
  .wordmark{position:absolute;left:0;right:0;top:46px;text-align:center;white-space:nowrap;
            font-family:"Montserrat",sans-serif;font-weight:800;font-size:34px;line-height:1;
            color:var(--wordmark);letter-spacing:-.5px}
  .rooftops{position:absolute;left:0;right:0;bottom:0;height:150px;
            background:linear-gradient(100deg,#080808 0%,#111 45%,#3a3a3a 75%,#1b1b1b 100%)}
</style>
</head>
<body>
  <section class="card card--front" aria-label="Card front">
    <div class="brand-panel">
      <span class="brand-mark"></span>
      <span class="brand-name">RIDGECREST ROOFING</span>
    </div>
    <div class="divider"></div>
    <div class="contact">
      <p class="contact__name">CARLA BENNING</p>
      <p class="contact__role">President</p>
      <p>18340 Harbor View Lane</p>
      <p>Seacliff CA 90417</p>
      <p class="contact__license">License number KMT48395</p>
      <p class="contact__line">
        <svg viewBox="0 0 24 24"><path fill="#1f7fc0" d="M6.6 10.8a15 15 0 0 0 6.6 6.6l2.2-2.2c.3-.3.7-.4 1-.2 1.1.4 2.3.6 3.6.6.6 0 1 .4 1 1V20c0 .6-.4 1-1 1A17 17 0 0 1 3 4c0-.6.4-1 1-1h3.5c.6 0 1 .4 1 1 0 1.3.2 2.5.6 3.6.1.3 0 .7-.2 1z"/></svg>
        555-240-0187</p>
      <p class="contact__line">
        <svg viewBox="0 0 24 24"><rect x="2" y="5" width="20" height="14" rx="2" fill="#1f7fc0"/><path d="M3 6l9 7 9-7" stroke="#161616" stroke-width="2" fill="none"/></svg>
        cbenning@ridgecrestroofing.com</p>
      <p class="contact__line">
        <svg viewBox="0 0 24 24"><circle cx="12" cy="12" r="10" fill="#1f7fc0"/><path d="M2 12h20M12 2c3 3 3 17 0 20M12 2c-3 3-3 17 0 20" stroke="#161616" stroke-width="1.5" fill="none"/></svg>
        www.ridgecrestroofing.com</p>
    </div>
    <div class="badge" aria-label="Accreditation badge"></div>
  </section>

  <section class="card card--back" aria-label="Card back">
    <p class="wordmark">RIDGECREST ROOFING</p>
    <div class="rooftops" role="img" aria-label="Dark silhouette of house rooftops with gables and windows"></div>
  </section>
</body>
</html>
```